Kestrel Photography Business Card

I need a business card designed for a photography business based in Perth, Western Australia called Kestrel Photography.

We specialise in wedding, event photography and portrait photography.

The business card must borrow the style of the attached logo.

The hex codes for the colours in the logo are:
#ED1D85 - Pink
#89C23E - Green
#37282F - Black

The name on the card will be:
Name: Toviran
Phone: 0417395268
Website: www.kestrelphotography.com.au
Facebook: kestrelphotography

I am open and happy to accept creative concepts.

I’d like some space at the back for writing notes and appointment details.

```html
<!DOCTYPE html>
<html lang="en">
<head>
<meta charset="utf-8">
<title>Kestrel Photography Business Card</title>
<link rel="stylesheet" href="https://fonts.googleapis.com/css2?family=Questrial&display=swap">
<style>
  :root {
    --pink: #ED1D85;
    --green: #89C23E;
    --green-light: #9CCB5B;
    --ink: #37282F;
    --white: #FFFFFF;
    --page: #FFFFFF;
    --rule: rgba(255, 255, 255, 0.55);
    --front-edge: #E6E6E6;
  }
  * { margin: 0; padding: 0; box-sizing: border-box; }
  html, body {
    width: 1063px;
    height: 1200px;
    overflow: hidden;
    background: var(--page);
    font-family: "Questrial", sans-serif;
  }
  .canvas {
    position: relative;
    width: 1063px;
    height: 1200px;
  }
  .card {
    position: absolute;
    border-radius: 28px;
    overflow: hidden;
  }

  /* Front */
  .card-front {
    left: 110px;
    top: 84px;
    width: 852px;
    height: 469px;
    background: var(--white);
    border: 1px solid var(--front-edge);
  }
  .brand-mark {
    position: absolute;
    left: 348px;
    top: 174px;
    width: 168px;
    height: 168px;
    border-radius: 50%;
    background: var(--pink);
  }
  .brand-name {
    position: absolute;
    left: 0;
    right: 0;
    top: 388px;
    text-align: center;
    font-size: 26px;
    letter-spacing: 0.55em;
    text-indent: 0.55em;
    color: var(--ink);
    text-transform: uppercase;
    white-space: nowrap;
  }

  /* Back */
  .card-back {
    left: 99px;
    top: 636px;
    width: 854px;
    height: 470px;
    background: var(--green);
    color: var(--white);
  }
  .back-accent {
    position: absolute;
    left: -80px;
    top: 116px;
    width: 250px;
    height: 250px;
    border-radius: 50%;
    background: var(--pink);
  }
  .contact {
    position: absolute;
    left: 224px;
    top: 96px;
    font-size: 26px;
    line-height: 38px;
  }
  .notes-panel {
    position: absolute;
    left: 224px;
    top: 190px;
    right: 0;
    height: 127px;
    background: var(--green-light);
  }
  .notes-label {
    position: absolute;
    left: 26px;
    top: 44px;
    font-size: 14px;
  }
  .notes-line {
    position: absolute;
    left: 26px;
    right: 0;
    height: 1px;
    background: var(--rule);
  }
  .notes-line.first { top: 60px; }
  .notes-line.second { top: 93px; }
  .web-links {
    position: absolute;
    right: 34px;
    top: 350px;
    text-align: right;
    font-size: 28px;
    line-height: 40px;
  }
  .social {
    display: inline-flex;
    align-items: center;
    gap: 10px;
  }
  .social-square {
    display: inline-block;
    width: 33px;
    height: 33px;
    border-radius: 4px;
    background: #3B5A9A;
  }
</style>
</head>
<body>
<main class="canvas">
  <section class="card card-front" aria-label="Card front">
    <div class="brand-mark" role="img" aria-label="Kestrel Photography brand mark"></div>
    <p class="brand-name">Kestrel Photography</p>
  </section>

  <section class="card card-back" aria-label="Card back">
    <div class="back-accent" role="img" aria-label="Large brand mark decoration"></div>
    <div class="contact">
      <p>NAME. Toviran</p>
      <p>PHONE. 0417395268</p>
    </div>
    <div class="notes-panel">
      <span class="notes-label">(notes)</span>
      <span class="notes-line first"></span>
      <span class="notes-line second"></span>
    </div>
    <div class="web-links">
      <p>www.kestrelphotography.com.au</p>
      <p class="social">kestrelphotography <span class="social-square" aria-hidden="true"></span></p>
    </div>
  </section>
</main>
</body>
</html>
```